The Gemstone Craft Studio Sales Business Card

The goal of this project is to create a interactive & effective business card design for SALES purposes with the intention to get customer on to our website and make a purchase or contact us about a product or service.
Website: WWW.RINGFORGEHUB.COM
GoogleMyBusiness: https://g.page/RingForgeHUB?gm
Facebook & Instagram: @THEGEMSTONECRAFTSTUDIO
Phone # & Text Message & Whatsapp Message: +1(555) 418-0293
Email: HELLO@RINGFORGEHUB.COM
Location: 4872 Brambleton Avenue Suite 512 Fairhollow, VT
(It would be necessary to have the appropriate ticker/icon for each social media platform as well as the location ticker and phone / messaging icons instead of spelling the words out.)
It is important to have the company logo and details but with an emphasis toward website. Feel free to also completely make one design your way and completely custom as you feel best.
The Gemstone Craft Studio is a Provider of Luxury Goods & Services such as: Custom Jewelry Design, Jewelry Repairs & Cleaning, Designer Jewelry, Luxury Gifts, 24 Karat Gold, 22 Karat Gold Jewelry, Diamond Jewelry, Insured Jewelry Appraisals, Loose Gemstones & Diamonds, Supporting Sustainability
Target Market(s)
People looking to invest in precious metals and gemstones as well as people looking to find a gift for a loved one for a special occasion. Customers looking to Custom Design Jewelry.
Contact Information for Business Card
Font styles to use
Other font styles liked:
- w.e you want
Colors
Designer to choose colors to be used in the design.
Requirements
Must have
- Website: WWW.RINGFORGEHUB.COM
- GoogleMyBusiness: https://g.page/RingForgeHUB?gm
- Facebook & Instagram: @THEGEMSTONECRAFTSTUDIO
- Phone # & Text Message & Whatsapp Message: +1(555) 418-0293
- Email: HELLO@RINGFORGEHUB.COM
- Location: 4872 Brambleton Avenue Suite 512 Fairhollow, VT
- (It would be necessary to have the appropriate ticker/icon for each social media platform as well as the location ticker and phone / messaging icons instead of spelling the words out.)
- It is important to have the company logo and details but with an emphasis toward website. Feel free to also completely make one design your way and completely custom as you feel best.
Nice to have
- The Gemstone Craft Studio is a Provider of Luxury Goods & Services such as: Custom Jewelry Design, Jewelry Repairs & Cleaning, Designer Jewelry, Luxury Gifts, 24 Karat Gold, 22 Karat Gold Jewelry, Diamond Jewelry, Insured Jewelry Appraisals, Loose Gemstones & Diamonds, Supporting Sustainability

```html
<!DOCTYPE html>
<html lang="en">
<head>
<meta charset="utf-8">
<title>The Gemstone Craft Studio – Business Card</title>
<link href="https://fonts.googleapis.com/css2?family=Cinzel:wght@600&family=Arimo:wght@400&display=swap" rel="stylesheet">
<style>
  :root {
    --ruby: #dc1f2a;
    --gold: #d9b06a;
    --paper: #fbfafb;
    --ink: #1a1a1a;
    --backdrop: #2a2a2a;
  }
  * { box-sizing: border-box; margin: 0; padding: 0; }
  html, body { width: 1200px; height: 900px; overflow: hidden; }
  body {
    background: var(--backdrop);
    font-family: "Arimo", Arial, sans-serif;
    color: var(--ink);
    position: relative;
  }
  .card {
    position: absolute;
    left: 230px;
    width: 740px;
    height: 420px;
    background: var(--paper);
    overflow: hidden;
  }
  .card--front { top: 20px; }
  .card--back { top: 460px; }

  /* Front */
  .brand {
    font-family: "Cinzel", serif;
    font-weight: 600;
    color: var(--ruby);
    display: flex;
    align-items: center;
    gap: 18px;
  }
  .brand__dot {
    width: 70px; height: 70px;
    border-radius: 50%;
    background: var(--gold);
    flex: none;
  }
  .card--front .brand {
    position: absolute;
    top: 90px; left: 0; right: 0;
    justify-content: center;
    font-size: 40px;
    line-height: 1.05;
  }
  .services {
    position: absolute;
    top: 240px; left: 20px; right: 20px;
    text-align: center;
    font-size: 14px;
    line-height: 1.35;
  }
  .services__lead { font-size: 17px; margin-bottom: 3px; }
  .services__line { display: block; white-space: nowrap; }

  /* Back */
  .card--back .brand {
    position: absolute;
    top: 36px; left: 42px;
    font-size: 34px;
    line-height: 1.05;
  }
  .contacts {
    position: absolute;
    top: 150px; left: 42px;
    list-style: none;
  }
  .contacts li {
    display: flex;
    align-items: center;
    gap: 12px;
    font-size: 16px;
    height: 28px;
    white-space: nowrap;
  }
  .icon {
    width: 22px; height: 22px;
    flex: none;
  }
  .decor-circle {
    position: absolute;
    right: 60px; top: 110px;
    width: 210px; height: 210px;
    border-radius: 50%;
    background: var(--gold);
  }
  .footer-band {
    position: absolute;
    left: 0; bottom: 0;
    width: 740px; height: 80px;
  }
  .website {
    position: absolute;
    right: 40px; bottom: 22px;
    color: #fff;
    font-size: 19px;
    letter-spacing: 2px;
  }
</style>
</head>
<body>

<section class="card card--front">
  <div class="brand">
    <span class="brand__dot"></span>
    <span>The Gemstone<br>Craft Studio</span>
  </div>
  <div class="services">
    <p class="services__lead">The Gemstone Craft Studio is a Provider of Luxury Goods &amp; Services such as:</p>
    <p>
      <span class="services__line">Custom Jewelry Design, Jewelry Repairs &amp; Cleaning, Designer Jewelry, Luxury Gifts, 24 Karat Gold,</span>
      <span class="services__line">22 Karat Gold Jewelry, Diamond Jewelry, Insured Jewelry Appraisals,</span>
      <span class="services__line">Loose Gemstones &amp; Diamonds, Supporting Sustainability</span>
    </p>
  </div>
</section>

<section class="card card--back">
  <div class="brand">
    <span>The Gemstone<br>Craft Studio</span>
  </div>

  <ul class="contacts">
    <li>
      <svg class="icon" viewBox="0 0 24 24"><circle cx="12" cy="12" r="11" fill="none" stroke="#dc1f2a" stroke-width="1.5"/><path d="M8 7l2 0 1 3-1.5 1a7 7 0 0 0 3.5 3.5l1-1.5 3 1v2a1 1 0 0 1-1 1A10 10 0 0 1 7 8a1 1 0 0 1 1-1z" fill="#d9b06a"/></svg>
      +1(555) 418-0293
    </li>
    <li>
      <svg class="icon" viewBox="0 0 24 24"><circle cx="12" cy="12" r="11" fill="none" stroke="#dc1f2a" stroke-width="1.5"/><circle cx="12" cy="12" r="5" fill="#d9b06a"/></svg>
      +1(555) 418-0293
    </li>
    <li>
      <svg class="icon" viewBox="0 0 24 24"><circle cx="12" cy="12" r="11" fill="none" stroke="#dc1f2a" stroke-width="1.5"/><circle cx="12" cy="12" r="5" fill="#d9b06a"/></svg>
      https://g.page/RingForgeHUB?gm
    </li>
    <li>
      <svg class="icon" viewBox="0 0 24 24"><circle cx="12" cy="12" r="11" fill="none" stroke="#dc1f2a" stroke-width="1.5"/><rect x="6" y="8" width="12" height="8" fill="none" stroke="#d9b06a" stroke-width="1.5"/><path d="M6 8l6 5 6-5" fill="none" stroke="#d9b06a" stroke-width="1.5"/></svg>
      HELLO@RINGFORGEHUB.COM
    </li>
    <li>
      <svg class="icon" viewBox="0 0 24 24"><circle cx="12" cy="12" r="11" fill="none" stroke="#dc1f2a" stroke-width="1.5"/><circle cx="12" cy="12" r="5" fill="#d9b06a"/></svg>
      @THEGEMSTONECRAFTSTUDIO
    </li>
    <li>
      <svg class="icon" viewBox="0 0 24 24"><circle cx="12" cy="12" r="11" fill="none" stroke="#dc1f2a" stroke-width="1.5"/><circle cx="12" cy="12" r="5" fill="#d9b06a"/></svg>
      @THEGEMSTONECRAFTSTUDIO
    </li>
    <li>
      <svg class="icon" viewBox="0 0 24 24"><circle cx="12" cy="12" r="11" fill="none" stroke="#dc1f2a" stroke-width="1.5"/><path d="M12 5a4.5 4.5 0 0 0-4.5 4.5C7.5 13 12 18 12 18s4.5-5 4.5-8.5A4.5 4.5 0 0 0 12 5z" fill="#d9b06a"/><circle cx="12" cy="9.5" r="1.6" fill="#fbfafb"/></svg>
      4872 Brambleton Avenue Suite 512 Fairhollow, VT
    </li>
  </ul>

  <div class="decor-circle"></div>

  <svg class="footer-band" viewBox="0 0 740 80" preserveAspectRatio="none">
    <rect x="0" y="22" width="440" height="4" fill="#d9b06a"/>
    <path d="M0 34 H430 Q450 34 460 22 Q472 10 500 10 H740 V80 H0 Z" fill="#dc1f2a"/>
  </svg>
  <div class="website">WWW.RINGFORGEHUB.COM</div>
</section>

</body>
</html>
```